Design personal page for IT Expert

I'm freelancer in the area of IT Architecture/Cloud Computing/DevOps. <br/>Already have own page: www.brevantu.cc<br/><br/>I want to update/redesign it and have following sections/pages there:<br/>1) My short bio/details/soft skills<br/>2) List of my hard skills<br/>3) My key clients/success stories/feedbacks<br/>4) List of my conference talks with links/embedded youtube video<br/>5) List of my articles with links (probably article text on sub-page like blog)<br/><br/>Design should be compatible with wix.com (gona have premium plan there)<br/>

Number of Pages Required

4 page

Font styles to use
Sans Serif

Colors

Designer to choose colors to be used in the design.

Requirements
Must have
• 1) My short bio/details/soft skills
• 2) List of my hard skills
• 3) My key clients/success stories/feedbacks
• 4) List of my conference talks with links/embedded youtube video
• 5) List of my articles with links (probably article text on sub-page like blog)
Should not have
• No direct contact to my skype/email. I prefer to use this platform for my task discussion.

```html
<!DOCTYPE html>
<html lang="en">
<head>
<meta charset="utf-8">
<title>Danil Vorontek — Cloud DevOps &amp; Architect</title>
<link rel="stylesheet" href="https://fonts.googleapis.com/css2?family=League+Spartan:wght@700;800&family=Hind:wght@300;400;500;600&display=swap">
<style>
  :root {
    --bg: #1f2337;
    --bg-deep: #1b1f31;
    --accent: #f5c07a;
    --text: #ffffff;
    --line: rgba(255, 255, 255, 0.35);
    --photo-warm: #b98a5e;
    --photo-grey: #9a9ca3;
  }
  * { margin: 0; padding: 0; box-sizing: border-box; }
  html, body {
    width: 1200px;
    height: 675px;
    overflow: hidden;
    background: var(--bg);
  }
  .hero {
    position: relative;
    width: 1200px;
    height: 675px;
    background: var(--bg);
    overflow: hidden;
    font-family: "Hind", sans-serif;
    color: var(--text);
  }
  .hero__lines {
    position: absolute;
    inset: 0;
  }
  .brand {
    position: absolute;
    left: 87px;
    top: 43px;
    font-family: "League Spartan", sans-serif;
    font-weight: 700;
    font-size: 15px;
    line-height: 17px;
    color: var(--accent);
  }
  .nav {
    position: absolute;
    top: 41px;
    right: 96px;
    display: flex;
    align-items: center;
    gap: 29px;
  }
  .nav__link {
    font-family: "Hind", sans-serif;
    font-weight: 500;
    font-size: 16.5px;
    color: var(--text);
    text-decoration: none;
    padding-top: 3px;
  }
  .nav__cta {
    margin-left: -12px;
    width: 113px;
    height: 37px;
    border: 1.5px solid var(--accent);
    border-radius: 3px;
    color: var(--accent);
    font-weight: 400;
    font-size: 16px;
    letter-spacing: 0.3px;
    display: flex;
    align-items: center;
    justify-content: center;
    padding-top: 3px;
    text-decoration: none;
  }
  .intro {
    position: absolute;
    left: 87px;
    top: 202px;
  }
  .intro__greeting {
    font-weight: 300;
    font-size: 40px;
    line-height: 46px;
    color: var(--accent);
  }
  .intro__first {
    font-family: "League Spartan", sans-serif;
    font-weight: 800;
    font-size: 133px;
    line-height: 1;
    margin-top: 4px;
    margin-left: -3px;
    letter-spacing: -1px;
    height: 104px;
  }
  .intro__last {
    font-family: "League Spartan", sans-serif;
    font-weight: 800;
    font-size: 84px;
    line-height: 1;
    margin-top: 17px;
    margin-left: -3px;
    height: 70px;
  }
  .intro__role {
    margin-top: 17px;
    font-weight: 300;
    font-size: 26px;
    line-height: 30px;
  }
  .portrait {
    position: absolute;
    left: 650px;
    top: 149px;
    width: 530px;
    height: 526px;
    border-radius: 46% 46% 12% 12% / 40% 40% 0 0;
    background: linear-gradient(180deg, var(--photo-warm) 0%, #a47a55 50%, var(--photo-grey) 80%, #8d8f96 100%);
    clip-path: polygon(35% 0, 65% 0, 90% 30%, 94% 62%, 100% 100%, 0 100%, 8% 62%, 12% 30%);
  }
</style>
</head>
<body>
<main class="hero">
  <svg class="hero__lines" width="1200" height="675" viewBox="0 0 1200 675" aria-hidden="true">
    <polygon points="3,675 269,212 534,675" fill="var(--bg-deep)" stroke="var(--line)" stroke-width="0.8"/>
    <polygon points="175,675 354,362 534,675" fill="var(--bg)" stroke="var(--line)" stroke-width="0.8"/>
  </svg>

  <div class="brand">YOUR<br>LOGO</div>

  <nav class="nav">
    <a class="nav__link" href="#home">HOME</a>
    <a class="nav__link" href="#about">ABOUT ME</a>
    <a class="nav__link" href="#skills">MY SKILLS</a>
    <a class="nav__cta" href="#chat">LET'S CHAT</a>
  </nav>

  <section class="intro">
    <p class="intro__greeting">Hello, I'm</p>
    <h1>
      <span class="intro__first" style="display:block">DANIL</span>
      <span class="intro__last" style="display:block">VORONTEK</span>
    </h1>
    <p class="intro__role">Stratus Cloud DevOps &amp; Architect<br>CI/CD Automation Expert</p>
  </section>

  <div class="portrait" role="img" aria-label="Portrait photo of a laughing person with curly hair in a grey hoodie"></div>
</main>
</body>
</html>
```